Need Eye Catching & Visually Stimulating/Out of the Box Web Design REFRESH for an Ecommerce W...

We need a new website design for our company Brindle Table (https://www.brindletable-demo.com/). We DO NOT WANT A BORING STANDARD SITE. This site has to be different, and has to POP!

Logo Files: https://files.example-share.net/folders/k7Qm2RtXw9LpZa4VbN8cYd3Hs6JfUe1Go?view=shared

Website Photos here: https://files.example-share.net/folders/9Tz-WqPl4Rk_bnMaYcVx28sdLhe73oj?view=shared

Websites we like:
https://morvenna.sitecraft-demo.io/
http://crumbvale.com/

We will need the site building Wordpress/Woocommerce and also help with interior pages & installation plug-ins -- see further attachments.

Information about the company:
1. PURPOSE: Why do we exist?
We believe that food is the root source to healthy living.
2. VISION: What future do we want to help create?
A world of healthy and happy people.
3. MISSION: What are we here to do?
Empower every person to utilize food as a means of living a healthy life.

Value Proposition:
Brindle Table develops new food based on the latest science to provide the human body with the proper nutrients for optimal health. Our research based foods target the key health functions that support healthy aging and active lifestyles. Since 2002, we have been innovating and designing our meals to meet the needs for healthy aging to active lifestyles. To help people perform their best, today & in the future.

Objective:
This is a nationwide issue and it's coming to the surface. Food affects people in a number of different ways. Our objective is to create an approachable and sustainable solution that can assist people with a number of ailments. The end result for all of them is feeling a feeling they haven't felt in quite some time. Feeling a refreshed you. Like water for fish, food for humans. Keep it clean and simple so you can focus on enjoying your life.

PHRASES/TAGLINES:
Empowerment Through Food
Real Food, Real Results
Nutrition Made Simple
Not Just Meal Prep, Food Science
A healthier you, delivered to your door
Increase your health and wellness baseline.
Discover the potential of healthier eating
Become the best version of you
It’s incredible what proper nutrition feels like
Taste & feel the difference. Your future self will thank you.
A healthier you is just a meal away
Life Changing results
Overwhelmed with being healthy, stops here.
Designed by doctors, approved by humans
Results Driven Healthy Eating, Delivered to you.
Become the person you deserve to be.
Enjoy the process of becoming a better you

Value Propositions:
We Educate & Empower People Through Food to Live Their Best Life
Sustainable health through proper nutrition… that’s enjoyable too.

Key Statements:
We provide satisfying meals that are nutrient dense & deliver results.
Our meals provide an easy way to enjoy an anti-inflammatory diet that's as satisfying as it is healthy.
Health, fat loss & feeling good through chef-prepared, nutrient-dense, satisfying meals delivered to your door.

PLEASE REVIEW THE ATTACHMENTS.

Industry/Entity Type

See Description & Attachments

Coding

Coded - Design and coding required

Number of Pages Required

5+ page

Font styles to use
Other font styles liked:
• See Description & Attachments

Colors
0094D4
00A9DD
6FCCEA
C7EBF8
E9F6FB
00AB8E
00BBA5
67D7C9
C6EFE9
E9F9F6

Requirements
Must have
Nice to have
Should not have

```html
<!DOCTYPE html>
<html lang="en">
<head>
<meta charset="utf-8">
<title>Brindle Table — Home</title>
<link href="https://fonts.googleapis.com/css2?family=Josefin+Sans:wght@400;600;700&family=Montserrat:wght@400;500;600&display=swap" rel="stylesheet">
<style>
:root{
  --forest:#03513f;
  --sage:#a9bc9b;
  --sage-soft:#c3d1b8;
  --olive:#c7c7a0;
  --card:#efefef;
  --ink:#2b2b2b;
  --muted:#5d5d5d;
  --white:#ffffff;
}
*{margin:0;padding:0;box-sizing:border-box}
html,body{width:1200px;height:4222px;overflow:hidden}
body{position:relative;background:var(--white);font-family:"Montserrat",sans-serif;color:var(--ink)}
.abs{position:absolute}
.heading{font-family:"Josefin Sans",sans-serif;font-weight:600;color:var(--forest);text-align:center;font-size:38px;width:100%;left:0}
.pill{position:absolute;border-radius:20px;font-family:"Josefin Sans",sans-serif;font-weight:600;font-size:12px;display:flex;align-items:center;justify-content:center;height:30px}
.pill--dark{background:var(--forest);color:var(--white)}
.pill--sage{background:var(--sage);color:var(--forest)}
.pill--pale{background:#cfd9c4;color:var(--forest)}
.photo{position:absolute}

/* header */
.site-header{position:absolute;top:0;left:0;width:1200px;height:74px;background:var(--white);z-index:5}
.brand-badge{position:absolute;left:197px;top:-60px;width:138px;height:168px;border-radius:0 0 70px 70px;background:var(--white);z-index:6;display:flex;flex-direction:column;align-items:center;justify-content:flex-end;padding-bottom:34px}
.brand-badge__dot{width:14px;height:14px;border-radius:50%;background:var(--forest);margin-bottom:6px}
.brand-badge__name{font-family:"Josefin Sans",sans-serif;font-weight:700;font-size:17px;color:var(--forest);line-height:1;text-align:center}
.main-nav{position:absolute;left:0;top:32px;width:1200px;height:14px;font-family:"Josefin Sans",sans-serif;font-size:10px;font-weight:600;color:var(--forest)}
.main-nav span{position:absolute;top:0;white-space:nowrap}
.main-nav .is-active{border-bottom:1px solid var(--forest)}
.icon-btn{position:absolute;top:22px;width:30px;height:30px;border-radius:50%;border:1.5px solid var(--forest)}
.cart-btn{position:absolute;left:912px;top:22px;width:88px;height:30px;border-radius:16px;background:var(--forest);color:var(--white);font-size:10px;font-weight:600;display:flex;align-items:center;justify-content:center;gap:6px}

/* hero */
.hero{position:absolute;top:74px;left:0;width:1200px;height:480px;background:linear-gradient(120deg,#6f8c7d 0%,#9bb4a6 35%,#b9c7bd 60%,#7d988a 100%)}
.hero__shade{position:absolute;inset:0;background:rgba(20,70,55,.35)}
.hero__title{position:absolute;top:200px;left:200px;width:800px;text-align:center;font-family:"Josefin Sans",sans-serif;font-weight:400;font-size:37px;line-height:45px;color:var(--white)}

/* how it works */
.step{position:absolute;top:660px;width:240px;text-align:center}
.step__icon{display:block;margin:0 auto 14px}
.step__title{font-family:"Josefin Sans",sans-serif;font-weight:600;font-size:15px;color:var(--forest);margin-bottom:12px}
.step__text{font-size:11px;line-height:15px;color:var(--ink)}

/* menu */
.menu-card{position:absolute;width:181px;height:171px;background:var(--card);overflow:hidden}
.menu-card__img{height:133px}
.menu-card__label{height:38px;display:flex;align-items:center;justify-content:center;font-family:"Josefin Sans",sans-serif;font-weight:600;font-size:14px;color:var(--forest)}
.menu-card--active .menu-card__label{background:var(--forest);color:var(--white)}

/* stats */
.stat{position:absolute;top:1800px;width:206px;text-align:center;color:var(--white)}
.stat__num{font-family:"Josefin Sans",sans-serif;font-weight:600;font-size:30px}
.stat__label{font-size:13px;color:#a9c4b3;line-height:16px;margin-top:4px}
.stat-divider{position:absolute;top:1800px;width:1px;height:76px;background:#8fb3a1}

/* programs */
.program{position:absolute;top:2134px;width:250px;height:293px;border:1px solid #d8d8d8;background:var(--white);text-align:center}
.program__img{height:156px}
.program__title{font-family:"Josefin Sans",sans-serif;font-weight:600;font-size:15px;color:var(--forest);margin:22px 20px 0;line-height:16px}
.program__text{font-size:11px;line-height:15px;margin:20px 30px 0;color:var(--ink)}
.arrow{position:absolute}

/* mission */
.mission__title{position:absolute;left:200px;top:2645px;font-family:"Josefin Sans",sans-serif;font-weight:600;font-size:36px;color:var(--forest)}
.mission__text{position:absolute;left:200px;top:2708px;width:340px;font-size:18px;line-height:22px;color:var(--forest)}

/* testimonials */
.review{position:absolute;top:3103px;width:250px;height:268px;background:var(--card);text-align:center}
.review__quote{width:52px;height:52px;border-radius:50%;background:var(--forest);margin:30px auto 0;display:flex;align-items:center;justify-content:center;color:var(--white);font-family:"Josefin Sans",sans-serif;font-weight:700;font-size:22px}
.review__text{font-style:italic;font-size:11px;line-height:19px;margin:22px 22px 0;color:var(--ink)}
.review__name{font-family:"Josefin Sans",sans-serif;font-weight:600;font-size:13px;color:var(--forest);margin-top:18px}
.review__place{font-size:9.5px;margin-top:6px;color:var(--ink)}

/* newsletter */
.newsletter__input{position:absolute;left:344px;top:3681px;width:388px;height:36px;border-radius:18px;border:1.5px solid #9a9a7a;background:var(--white);font-size:11px;padding-left:16px;display:flex;align-items:center;color:#444}

/* footer */
.footer-brand{position:absolute;left:195px;top:3990px;font-family:"Josefin Sans",sans-serif;font-weight:600;font-size:32px;line-height:34px;color:var(--white);text-align:center;width:140px}
.footer-col{position:absolute;top:3948px;list-style:none;font-size:11px;color:#dfe9e3}
.footer-col li{height:30px}
.footer-col .is-current{text-decoration:underline;color:#9fbfae}
.social{position:absolute;left:969px;width:29px;height:29px;border-radius:50%;border:1.5px solid #7fa896}
.social--filled{background:#9fbfae;border-color:#9fbfae}
.copyright{position:absolute;top:4148px;left:0;width:100%;text-align:center;font-size:10px;color:var(--white)}
</style>
</head>
<body>

<header class="site-header">
  <nav class="main-nav">
    <span class="is-active" style="left:405px">— Home —</span>
    <span style="left:474px">Shop Now</span>
    <span style="left:544px">About</span>
    <span style="left:596px">Menu</span>
    <span style="left:645px">Programs</span>
    <span style="left:712px">FAQ</span>
    <span style="left:756px">Contact Us</span>
  </nav>
  <span class="icon-btn" style="left:836px" aria-label="Search">
    <svg width="27" height="27" viewBox="0 0 27 27"><circle cx="12.5" cy="12.5" r="3.5" fill="none" stroke="#03513f" stroke-width="1.6"/><line x1="15" y1="15" x2="18" y2="18" stroke="#03513f" stroke-width="1.6"/></svg>
  </span>
  <span class="icon-btn" style="left:874px" aria-label="Account">
    <svg width="27" height="27" viewBox="0 0 27 27"><circle cx="13.5" cy="11" r="3" fill="#03513f"/><path d="M8.5 19c0-3 2.2-4.5 5-4.5s5 1.5 5 4.5z" fill="#03513f"/></svg>
  </span>
  <span class="cart-btn">
    <svg width="12" height="11" viewBox="0 0 12 11"><path d="M0 1h2l1.6 6h6.4l1.5-4.5H3" fill="none" stroke="#fff" stroke-width="1.3"/><circle cx="4.5" cy="9.5" r="1" fill="#fff"/><circle cx="9" cy="9.5" r="1" fill="#fff"/></svg>
    $0.00
  </span>
</header>
<div class="brand-badge">
  <span class="brand-badge__dot"></span>
  <span class="brand-badge__name">Brindle<br>Table</span>
</div>

<section class="hero" role="img" aria-label="Photo of plated fresh salads, grilled fish and vegetables">
  <div class="hero__shade"></div>
</section>
<h1 class="hero__title">We provide satisfying meals that are nutrient dense &amp; deliver results.</h1>
<span class="pill pill--pale" style="left:545px;top:384px;width:110px">Get Started</span>
<svg class="abs" style="left:0;top:460px" width="1200" height="100" viewBox="0 0 1200 100" preserveAspectRatio="none"><path d="M0 60 C120 40 220 70 330 62 C460 52 520 72 640 66 C780 58 860 40 980 50 C1080 58 1140 30 1200 40 V100 H0Z" fill="#fff"/></svg>

<h2 class="heading abs" style="top:600px">How it works</h2>
<div class="step" style="left:203px">
  <svg class="step__icon" width="72" height="66" viewBox="0 0 72 66"><path d="M36 2c10 0 15 8 14 16 10-1 20 6 20 20 0 16-12 26-34 26S2 54 2 38c0-14 10-21 20-20C21 10 26 2 36 2z" fill="#a9bc9b"/><path d="M22 42l6 6 12-12M32 48l12-12" fill="none" stroke="#03513f" stroke-width="2"/></svg>
  <div class="step__title">Choose your meals</div>
  <p class="step__text">Lorem Ipsum is simply dummy text of the printing and typesetting industry.</p>
</div>
<div class="step" style="left:480px">
  <svg class="step__icon" width="72" height="66" viewBox="0 0 72 66"><path d="M36 2c10 0 15 8 14 16 10-1 20 6 20 20 0 16-12 26-34 26S2 54 2 38c0-14 10-21 20-20C21 10 26 2 36 2z" fill="#a9bc9b"/><rect x="26" y="32" width="20" height="4" rx="2" fill="none" stroke="#03513f" stroke-width="1.8"/><rect x="26" y="39" width="20" height="4" rx="2" fill="none" stroke="#03513f" stroke-width="1.8"/><path d="M26 30a10 6 0 0 1 20 0z" fill="none" stroke="#03513f" stroke-width="1.8"/></svg>
  <div class="step__title">Make it your own</div>
  <p class="step__text">Lorem Ipsum is simply dummy text of the printing and typesetting industry.</p>
</div>
<div class="step" style="left:755px">
  <svg class="step__icon" width="72" height="66" viewBox="0 0 72 66"><path d="M36 2c10 0 15 8 14 16 10-1 20 6 20 20 0 16-12 26-34 26S2 54 2 38c0-14 10-21 20-20C21 10 26 2 36 2z" fill="#a9bc9b"/><path d="M26 36h5v12h-5zM31 36l5-8c2 0 3 1 3 3l-1 4h7c2 0 3 2 2 3l-2 8c0 1-1 2-3 2h-11" fill="none" stroke="#03513f" stroke-width="1.8"/></svg>
  <div class="step__title">Fresh and affordable</div>
  <p class="step__text">Lorem Ipsum is simply dummy text of the printing and typesetting industry.</p>
</div>
<span class="pill pill--dark" style="left:544px;top:837px;width:112px">Get Started</span>

<!-- menu band -->
<svg class="abs" style="left:0;top:930px" width="1200" height="60" viewBox="0 0 1200 60" preserveAspectRatio="none"><path d="M0 60 V30 C150 20 260 10 420 20 C560 30 620 5 760 12 C900 18 1000 10 1200 25 V60Z" fill="#a9bc9b"/></svg>
<div class="abs" style="left:0;top:988px;width:1200px;height:680px;background:var(--sage)"></div>
<h2 class="heading abs" style="top:1033px">Explore our menu</h2>

<div class="menu-card" style="left:200px;top:1096px"><div class="menu-card__img" role="img" aria-label="Photo of chicken meal in a black tray" style="background:linear-gradient(135deg,#ffd6a0,#6b4b2e 55%,#2d3b22)"></div><div class="menu-card__label">Chicken</div></div>
<div class="menu-card menu-card--active" style="left:406px;top:1096px"><div class="menu-card__img" role="img" aria-label="Photo of turkey bowl with green beans and rice" style="background:radial-gradient(circle at 50% 55%,#6e5a3c,#2a2a26 60%,#e7d9c2)"></div><div class="menu-card__label">Turkey</div></div>
<div class="menu-card" style="left:613px;top:1096px"><div class="menu-card__img" role="img" aria-label="Photo of beef with roasted peppers and broccoli" style="background:linear-gradient(160deg,#f2f2f2,#b9432a 40%,#6b3b22 70%,#5f8a3a)"></div><div class="menu-card__label">Beef</div></div>
<div class="menu-card" style="left:820px;top:1096px"><div class="menu-card__img" role="img" aria-label="Photo of seafood fillet with cauliflower mash" style="background:linear-gradient(150deg,#f4f1ea,#d2713d 50%,#e9e3d6)"></div><div class="menu-card__label">Seafood</div></div>
<div class="menu-card" style="left:200px;top:1293px"><div class="menu-card__img" role="img" aria-label="Photo of salad bowl with colourful vegetables" style="background:radial-gradient(circle at 55% 50%,#7a3a6a,#6b9a3a 45%,#7dfa9a 75%)"></div><div class="menu-card__label">Salads</div></div>
<div class="menu-card" style="left:406px;top:1293px"><div class="menu-card__img" role="img" aria-label="Photo of vegan squash and chickpea dish" style="background:linear-gradient(140deg,#e0a020,#c8741a 50%,#8a6a20)"></div><div class="menu-card__label">Vegan</div></div>
<div class="menu-card" style="left:613px;top:1293px"><div class="menu-card__img" role="img" aria-label="Photo of breakfast pancakes and grapes on a plate" style="background:radial-gradient(circle at 50% 55%,#d9a05a,#2e2e2e 55%,#f3f3f3)"></div><div class="menu-card__label">Breakfast</div></div>
<div class="menu-card" style="left:820px;top:1293px"><div class="menu-card__img" role="img" aria-label="Photo of coconut protein snack balls" style="background:linear-gradient(150deg,#f1ece6,#8a6a55 50%,#d9cfc6)"></div><div class="menu-card__label">Snacks</div></div>
<span class="pill pill--dark" style="left:537px;top:1496px;width:126px">View Full Menu</span>

<!-- award band -->
<svg class="abs" style="left:0;top:1570px" width="1200" height="100" viewBox="0 0 1200 100" preserveAspectRatio="none"><path d="M0 100 V70 C110 70 170 4 250 6 C330 8 360 78 450 78 C540 78 560 22 640 28 C720 34 750 88 840 84 C930 80 980 8 1070 18 C1130 26 1160 55 1200 48 V100Z" fill="#03513f"/></svg>
<div class="abs" style="left:0;top:1668px;width:1200px;height:336px;background:var(--forest)"></div>
<h2 class="heading abs" style="top:1728px;color:#fff">Award winning meals</h2>
<div class="stat" style="left:187px"><div class="stat__num">150K</div><div class="stat__label">Happy clients</div></div>
<div class="stat-divider" style="left:393px"></div>
<div class="stat" style="left:394px"><div class="stat__num">500K</div><div class="stat__label">Meals served nation<br>wide</div></div>
<div class="stat-divider" style="left:600px"></div>
<div class="stat" style="left:600px"><div class="stat__num">35+</div><div class="stat__label">Chef prepared<br>meals</div></div>
<div class="stat-divider" style="left:806px"></div>
<div class="stat" style="left:807px"><div class="stat__num">215</div><div class="stat__label">Awards</div></div>
<span class="pill pill--pale" style="left:544px;top:1911px;width:112px">Get Started</span>

<!-- programs -->
<h2 class="heading abs" style="top:2063px">Our programs</h2>
<svg class="arrow" style="left:140px;top:2272px" width="12" height="20" viewBox="0 0 12 20"><path d="M10 2L2 10l8 8" fill="none" stroke="#333" stroke-width="1.6"/></svg>
<svg class="arrow" style="left:1047px;top:2272px" width="12" height="20" viewBox="0 0 12 20"><path d="M2 2l8 8-8 8" fill="none" stroke="#333" stroke-width="1.6"/></svg>
<article class="program" style="left:200px"><div class="program__img" role="img" aria-label="Promo photo for the 21 day challenge with a group exercising" style="background:linear-gradient(180deg,#f3efe9,#c9b7a6 60%,#8a8a9a)"></div><h3 class="program__title">21 day challenge!</h3><p class="program__text">Get in shape and Feel<br>Your Best!</p></article>
<span class="pill pill--sage" style="left:268px;top:2411px;width:114px;height:28px">Buy Programs</span>
<article class="program" style="left:475px"><div class="program__img" role="img" aria-label="Promo photo for the parents meal program with an older couple" style="background:linear-gradient(180deg,#f2c400,#e6d79a 55%,#8bbb3a)"></div><h3 class="program__title">Take care of your loved<br>ones plan</h3><p class="program__text">Brindle Table has the perfect program for Mom &amp; Dad or any of your ...</p></article>
<span class="pill pill--dark" style="left:543px;top:2411px;width:114px;height:28px">Buy Programs</span>
<article class="program" style="left:749px"><div class="program__img" role="img" aria-label="Photo of braised beef with peppers and broccoli" style="background:linear-gradient(150deg,#e9e4df,#6b4030 45%,#b94228 65%,#5c8a36)"></div><h3 class="program__title">Medically tailored meals</h3><p class="program__text">Delicious, Nutritious<br>Food!</p></article>
<span class="pill pill--sage" style="left:817px;top:2411px;width:114px;height:28px">Buy Programs</span>

<!-- mission -->
<svg class="abs" style="left:0;top:2500px" width="1200" height="500" viewBox="0 0 1200 500" preserveAspectRatio="none">
  <defs><linearGradient id="missionPhoto" x1="0" y1="0" x2="1" y2="1"><stop offset="0" stop-color="#c9d1d4"/><stop offset=".45" stop-color="#d7dbdc"/><stop offset=".6" stop-color="#c26a28"/><stop offset=".8" stop-color="#b8d49a"/><stop offset="1" stop-color="#a07a50"/></linearGradient></defs>
  <path d="M0 50 C150 22 340 58 600 22 L600 430 C565 425 545 478 485 480 C420 482 400 404 330 410 C262 416 248 470 182 470 C122 470 92 408 42 410 C20 411 8 420 0 426Z" fill="#a9bc9b"/>
  <path role="img" aria-label="Photo of grilled chicken with roasted sweet potato and celery" d="M600 22 L1200 18 L1200 400 C1152 420 1122 462 1060 462 C982 462 960 390 880 400 C800 410 782 492 702 492 C652 492 632 440 600 430Z" fill="url(#missionPhoto)"/>
</svg>
<h2 class="mission__title">Our mission</h2>
<p class="mission__text">Educate &amp; empower people through food to live their best life.</p>
<span class="pill pill--dark" style="left:200px;top:2770px;width:114px">Contact Us</span>

<!-- testimonials -->
<h2 class="heading abs" style="top:3038px">What our clients say</h2>
<svg class="arrow" style="left:135px;top:3220px" width="12" height="20" viewBox="0 0 12 20"><path d="M10 2L2 10l8 8" fill="none" stroke="#333" stroke-width="1.6"/></svg>
<svg class="arrow" style="left:1051px;top:3220px" width="12" height="20" viewBox="0 0 12 20"><path d="M2 2l8 8-8 8" fill="none" stroke="#333" stroke-width="1.6"/></svg>
<article class="review" style="left:200px"><div class="review__quote">66</div><p class="review__text">"Lorem Ipsum is simply dummy text of the printing and typesetting industry. Lorem Ipsum has been the industry's standard dummy text ever printer took a galley."</p><div class="review__name">Harlan Vetch</div><div class="review__place">From South Fernbrook</div></article>
<article class="review" style="left:475px"><div class="review__quote">66</div><p class="review__text">"Lorem Ipsum is simply dummy text of the printing and typesetting industry. Lorem Ipsum has been the industry's standard dummy text ever printer took a galley."</p><div class="review__name">Owen Marlow</div><div class="review__place">From New Ashcombe</div></article>
<article class="review" style="left:749px"><div class="review__quote">66</div><p class="review__text">"Lorem Ipsum is simply dummy text of the printing and typesetting industry. Lorem Ipsum has been the industry's standard dummy text ever printer took a galley."</p><div class="review__name">Tessa Quill</div><div class="review__place">From North Fernbrook</div></article>
<span class="pill pill--dark" style="left:544px;top:3402px;width:112px">View All</span>

<!-- newsletter -->
<svg class="abs" style="left:0;top:3495px" width="1200" height="60" viewBox="0 0 1200 60" preserveAspectRatio="none"><path d="M0 60 V22 C180 32 320 12 520 18 C700 24 820 8 980 14 C1080 18 1150 10 1200 14 V60Z" fill="#c7c7a0"/></svg>
<div class="abs" style="left:0;top:3553px;width:1200px;height:300px;background:var(--olive)"></div>
<div class="photo" role="img" aria-label="Photo of a meal tray with steak, sweet potato and broccoli" style="left:-20px;top:3590px;width:250px;height:180px;border-radius:30px;transform:rotate(22deg);background:linear-gradient(135deg,#4a6a2a,#8a4a2a 45%,#d08a3a 70%,#2a2a2a)"></div>
<div class="photo" role="img" aria-label="Photo of a meal tray with steak, sweet potato and broccoli" style="left:950px;top:3590px;width:250px;height:180px;border-radius:30px;transform:rotate(-22deg);background:linear-gradient(225deg,#4a6a2a,#8a4a2a 45%,#d08a3a 70%,#2a2a2a)"></div>
<h2 class="heading abs" style="top:3616px">Join our newsletter</h2>
<div class="newsletter__input">Enter your email ...</div>
<span class="pill pill--dark" style="left:744px;top:3681px;width:112px;height:36px">Submit</span>

<!-- footer -->
<svg class="abs" style="left:0;top:3780px" width="1200" height="100" viewBox="0 0 1200 100" preserveAspectRatio="none"><path d="M0 100 V50 C70 46 110 80 190 72 C280 62 300 8 400 10 C500 12 520 72 620 68 C720 64 760 6 860 8 C960 10 990 74 1080 66 C1140 60 1170 40 1200 38 V100Z" fill="#03513f"/></svg>
<footer class="abs" style="left:0;top:3878px;width:1200px;height:344px;background:var(--forest)"></footer>
<div class="footer-brand">Brindle<br>Table</div>
<ul class="footer-col" style="left:406px"><li>My Account</li><li>Site Help</li><li>Shipping &amp; Returns</li><li>All Products</li><li>Gift Certificates</li></ul>
<ul class="footer-col" style="left:613px"><li>View Cart</li><li class="is-current">About Us</li><li>Corporate Catering</li><li>Podcast</li><li>Become an Affiliate</li></ul>
<ul class="footer-col" style="left:820px"><li>Order Status</li><li>Contact Us</li><li>Privacy Policy</li><li>Testimonials</li></ul>
<span class="social" style="top:3952px" aria-label="Social link"></span>
<span class="social social--filled" style="top:3990px" aria-label="Social link"></span>
<span class="social" style="top:4028px" aria-label="Social link"></span>
<span class="social" style="top:4066px" aria-label="Social link"></span>
<p class="copyright">© 2022 Brindle Table. All Rights Reserved.</p>

</body>
</html>
```